Wanderlark Gin - Bottle Label for a craft Gin about to be launched on the world from New Zealand

We are a start up craft distillery in New Zealand. We have developed a wonderful Gin using our own grain spirit and both traditional and New Zealand native botanicals (Manuka to be specific), chosen our bottle and the name "Wanderlark" and done a bit of amateur label design and now we are looking for someone to make it great.

Feel free to change up our amateur concept but give us something that will pop from the back bar and scream authenticity, craft and individuality.

The attached files give you the specifications of the bottle, our current concept for a Wanderlark label and an earlier concept drawing that gives an idea of where we are thinking the two labels should go on the front of the bottle.

Thanks, we look forward to your ideas!!

Target Market(s)

High end and craft Gin drinkers. Hipsters and cocktail barflys and their bar tenders and bar owners

Requirements
Must have
• Attractive individuality
Nice to have
• Coolness
Should not have
• Uncoolness

```html
<!DOCTYPE html>
<html lang="en">
<head>
<meta charset="utf-8">
<title>Wanderlark Gin – Bottle Label</title>
<link href="https://fonts.googleapis.com/css2?family=Jost:wght@200;300;400&display=swap" rel="stylesheet">
<style>
  :root {
    --page: #ffffff;
    --cream: #fcf8d6;
    --green: #6abd45;
    --sprig-on-cream: #dcedbd;
    --sprig-on-green: #8fcd6f;
    --ink: #231f20;
    --ink-shadow: #e6dfbd;
    --white: #ffffff;
    --glass-light: #fbfcfc;
    --glass-mid: #eceff0;
    --glass-edge: #d7dbdd;
  }
  html, body {
    margin: 0;
    padding: 0;
    overflow: hidden;
    background: var(--page);
  }
  .canvas {
    position: relative;
    width: 1200px;
    height: 1200px;
    overflow: hidden;
    background: var(--page);
    font-family: "Jost", sans-serif;
  }

  /* Bottle mock-up */
  .bottle {
    position: absolute;
    left: 130px;
    top: 185px;
    width: 228px;
    height: 842px;
  }
  .bottle__glass {
    position: absolute;
    left: 0;
    top: 0;
    width: 228px;
    height: 842px;
  }
  .bottle__label {
    position: absolute;
    left: 33px;
    top: 397px;
    width: 476px;
    height: 690px;
    transform: scale(0.349);
    transform-origin: 0 0;
  }

  /* Label */
  .label {
    position: absolute;
    left: 612px;
    top: 250px;
    width: 476px;
    height: 690px;
  }
  .label__top {
    position: absolute;
    left: 0;
    top: 0;
    width: 476px;
    height: 400px;
    background: var(--cream);
    border-radius: 78px 78px 0 0;
  }
  .label__bottom {
    position: absolute;
    left: 0;
    top: 420px;
    width: 476px;
    height: 270px;
    background: var(--green);
    border-radius: 0 0 92px 92px;
  }
  .botanicals {
    position: absolute;
    left: 40px;
    width: 396px;
    border-radius: 50px;
  }
  .botanicals--top {
    top: 22px;
    height: 118px;
    background: radial-gradient(ellipse at center, var(--sprig-on-cream) 0%, var(--cream) 72%);
  }
  .botanicals--bottom {
    top: 118px;
    height: 100px;
    background: radial-gradient(ellipse at center, var(--sprig-on-green) 0%, var(--green) 72%);
  }
  .brand-name {
    position: absolute;
    left: 0;
    top: 200px;
    width: 476px;
    margin: 0;
    text-align: center;
    font-weight: 300;
    font-size: 64px;
    line-height: 1;
    letter-spacing: 1px;
    color: var(--ink);
    text-shadow: 3px 3px 0 var(--ink-shadow);
  }
  .style-line {
    position: absolute;
    left: 0;
    top: 353px;
    width: 476px;
    margin: 0;
    text-align: center;
    font-weight: 300;
    font-size: 18px;
    line-height: 24px;
    letter-spacing: 0.3px;
    word-spacing: 3px;
    color: var(--green);
  }
  .volume {
    position: absolute;
    left: 0;
    top: 378px;
    width: 476px;
    margin: 0;
    text-align: center;
    font-weight: 300;
    font-size: 12px;
    line-height: 14px;
    letter-spacing: 1.5px;
    color: var(--green);
  }
  .description {
    position: absolute;
    left: 10px;
    top: 14px;
    width: 456px;
    margin: 0;
    text-align: center;
    font-weight: 300;
    font-size: 15.5px;
    line-height: 22px;
    color: var(--white);
  }
  .strength {
    position: absolute;
    top: 238px;
    margin: 0;
    font-weight: 300;
    font-size: 14.5px;
    line-height: 18px;
    color: var(--white);
  }
  .strength--proof { left: 103px; }
  .strength--abv { left: 258px; }
</style>
</head>
<body>
<main class="canvas">

  <figure class="bottle" aria-label="Label shown on a 500 ml glass bottle" style="margin:0">
    <svg class="bottle__glass" viewBox="0 0 228 842" role="img" aria-label="Clear glass gin bottle">
      <defs>
        <linearGradient id="glass-fill" x1="0" y1="0" x2="1" y2="0">
          <stop offset="0" stop-color="var(--glass-mid)"/>
          <stop offset="0.5" stop-color="var(--glass-light)"/>
          <stop offset="1" stop-color="var(--glass-mid)"/>
        </linearGradient>
      </defs>
      <path d="M73 6 H161 V60 L168 70 L170 230 Q172 262 212 276 L220 292 V812 L208 836 H20 L8 812 V292 L16 276 Q56 262 58 230 L60 70 L67 60 Z"
            fill="url(#glass-fill)" stroke="var(--glass-edge)" stroke-width="2"/>
    </svg>
    <div class="bottle__label" aria-hidden="true">
      <div class="label__top">
        <div class="botanicals botanicals--top"></div>
        <p class="brand-name">WANDERLARK</p>
        <p class="style-line">NEW ZEALAND SMALL BATCH GIN</p>
        <p class="volume">500 ml</p>
      </div>
      <div class="label__bottom">
        <p class="description">A classically inspired Gin with a New Zealand twist.&nbsp; Distilled<br>in-house starting with local grain and finished with 11<br>botanicals including a generous helping of East Coast Manuka<br>cones, Gisborne Citrus and Otago Lavender</p>
        <div class="botanicals botanicals--bottom"></div>
        <p class="strength strength--proof">84 PROOF</p>
        <p class="strength strength--abv">42% ALC. BY VOL.</p>
      </div>
    </div>
  </figure>

  <section class="label" aria-label="Wanderlark gin front label">
    <div class="label__top">
      <div class="botanicals botanicals--top" role="img" aria-label="Line drawing of manuka flowers, lavender sprigs and a citrus slice"></div>
      <h1 class="brand-name">WANDERLARK</h1>
      <p class="style-line">NEW ZEALAND SMALL BATCH GIN</p>
      <p class="volume">500 ml</p>
    </div>
    <div class="label__bottom">
      <p class="description">A classically inspired Gin with a New Zealand twist.&nbsp; Distilled<br>in-house starting with local grain and finished with 11<br>botanicals including a generous helping of East Coast Manuka<br>cones, Gisborne Citrus and Otago Lavender</p>
      <div class="botanicals botanicals--bottom" role="img" aria-label="Line drawing of manuka flowers, lavender sprigs and a citrus slice"></div>
      <p class="strength strength--proof">84 PROOF</p>
      <p class="strength strength--abv">42% ALC. BY VOL.</p>
    </div>
  </section>

</main>
</body>
</html>
```